Volren Goods Ltd Stationery Design Project

hi we need to design business cards, letter head, complimentary slips, scribble pads, note pads, envelopes for volren goods ltd.

please see business cards details

Kelvin Obutu

P.O Box 41873 -00312 Nairobi - Kenya
Tel: +254-733-218-904
Email: volrengoods@mailvexo.com

company name should appear on all stationery : Volren Goods Ltd

Industry/Entity Type

Business

Requirements
Must have
• kindly stick to colours in the logo

```html
<!DOCTYPE html>
<html lang="en">
<head>
<meta charset="utf-8">
<title>Volren Goods Ltd – Business Card</title>
<link rel="stylesheet" href="https://fonts.googleapis.com/css2?family=Quicksand:wght@500;700&display=swap">
<style>
  :root {
    --brand-orange: #f7941d;
    --brand-blue: #2e3a9a;
    --card-white: #ffffff;
    --ink: #1c1c1c;
    --backdrop: #e9e9ec;
    --card-shadow: 0 10px 28px rgba(0, 0, 0, 0.18);
  }
  * { box-sizing: border-box; margin: 0; padding: 0; }
  html, body {
    width: 1200px;
    height: 873px;
    overflow: hidden;
    background: var(--backdrop);
    font-family: "Quicksand", sans-serif;
  }
  .sheet {
    position: relative;
    width: 1200px;
    height: 873px;
    display: flex;
    align-items: center;
    justify-content: center;
    gap: 40px;
  }
  .card {
    position: relative;
    width: 540px;
    height: 310px;
    background: var(--card-white);
    box-shadow: var(--card-shadow);
    overflow: hidden;
  }
  .card-bands {
    position: absolute;
    inset: 0;
    width: 100%;
    height: 100%;
  }
  .band-orange { fill: var(--brand-orange); }
  .band-blue { fill: var(--brand-blue); }

  .brand {
    position: absolute;
    display: flex;
    align-items: center;
    gap: 12px;
  }
  .brand-dot {
    border-radius: 50%;
    background: var(--brand-orange);
    flex: none;
  }
  .brand-name {
    color: var(--brand-blue);
    font-weight: 700;
    text-transform: uppercase;
    line-height: 1;
    white-space: nowrap;
  }

  /* Front */
  .card--front .brand {
    left: 50%;
    top: 50%;
    transform: translate(-50%, -50%);
  }
  .card--front .brand-dot { width: 46px; height: 46px; }
  .card--front .brand-name { font-size: 44px; letter-spacing: 2px; }

  /* Back */
  .card--back .brand { left: 26px; top: 30px; }
  .card--back .brand-dot { width: 24px; height: 24px; }
  .card--back .brand-name { font-size: 24px; letter-spacing: 1px; }

  .brand-rule {
    position: absolute;
    left: 26px;
    top: 74px;
    width: 200px;
    height: 2px;
    background: var(--brand-blue);
  }
  .contact {
    position: absolute;
    left: 240px;
    top: 74px;
    padding-left: 14px;
    border-left: 2px solid var(--brand-blue);
    color: var(--ink);
    font-size: 15px;
    font-weight: 500;
    line-height: 1.55;
  }
  .contact-name {
    font-size: 17px;
    font-weight: 700;
    margin-bottom: 4px;
  }
</style>
</head>
<body>
  <main class="sheet">

    <!-- Contact side -->
    <section class="card card--back" aria-label="Business card, contact side">
      <svg class="card-bands" viewBox="0 0 540 310" preserveAspectRatio="none" aria-hidden="true">
        <polygon class="band-orange" points="0,258 250,258 214,310 0,310"/>
        <polygon class="band-blue" points="256,258 540,258 540,310 220,310"/>
      </svg>
      <div class="brand">
        <span class="brand-dot"></span>
        <span class="brand-name">Volren Goods</span>
      </div>
      <div class="brand-rule"></div>
      <address class="contact" style="font-style: normal;">
        <p class="contact-name">Kelvin Obutu</p>
        <p>P.O Box 41873 -00312</p>
        <p>Nairobi - Kenya</p>
        <p>Tel: +254-733-218-904</p>
        <p>Email: volrengoods@mailvexo.com</p>
      </address>
    </section>

    <!-- Brand side -->
    <section class="card card--front" aria-label="Business card, brand side">
      <svg class="card-bands" viewBox="0 0 540 310" preserveAspectRatio="none" aria-hidden="true">
        <path class="band-orange" d="M0,0 H540 V30 C420,44 300,22 180,30 C110,35 50,40 0,36 Z"/>
        <path class="band-blue" d="M0,268 C120,250 240,290 360,274 C430,265 490,262 540,266 V310 H0 Z"/>
      </svg>
      <div class="brand">
        <span class="brand-dot"></span>
        <span class="brand-name">Volren Goods</span>
      </div>
    </section>

  </main>
</body>
</html>
```